Verdant Harvest Collective - Business Card Design Project

We need business cards for our business. We grow roots and fruits in Central and South America, we import and distribute in FL, USA. We do fresh and frozen products.

Target Market(s)

Small and big supermarkets, wholesalers, traders, distributors, etc

Industry/Entity Type

Business

```html
<!DOCTYPE html>
<html lang="en">
<head>
<meta charset="utf-8">
<title>Verdant Harvest Collective – Business Card</title>
<link href="https://fonts.googleapis.com/css2?family=Open+Sans:wght@400;600;700&display=swap" rel="stylesheet">
<style>
  :root {
    --bg-mint: #9fd3c0;
    --bg-mint-light: #c8ddd2;
    --card-paper: #f1f1ef;
    --card-edge: #bfe6d8;
    --ink-dark: #2f3a2c;
    --ink-muted: #5d6459;
    --brand-green: #3f6b32;
    --leaf-tone: #dcdcd7;
    --rule: #7d8378;
  }
  html, body {
    margin: 0;
    width: 1200px;
    height: 818px;
    overflow: hidden;
  }
  body {
    background: linear-gradient(120deg, var(--bg-mint) 0%, var(--bg-mint-light) 100%);
    font-family: "Open Sans", Arial, sans-serif;
    position: relative;
  }
  .business-card {
    position: absolute;
    left: 250px;
    top: 209px;
    width: 700px;
    height: 400px;
    background: var(--card-paper);
    border-bottom: 10px solid var(--card-edge);
    box-sizing: border-box;
    overflow: hidden;
  }
  .leaf-motif {
    position: absolute;
    right: 30px;
    top: 40px;
    width: 300px;
    height: 330px;
    background: radial-gradient(ellipse at 55% 45%, var(--leaf-tone) 0%, rgba(220,220,215,0.5) 55%, rgba(241,241,239,0) 75%);
  }
  .card-header {
    position: absolute;
    left: 56px;
    right: 56px;
    top: 130px;
    display: flex;
    justify-content: space-between;
    align-items: baseline;
    gap: 24px;
  }
  .brand-name {
    display: flex;
    align-items: center;
    gap: 8px;
    font-size: 18px;
    font-weight: 600;
    color: var(--brand-green);
    white-space: nowrap;
  }
  .brand-dot {
    width: 10px;
    height: 10px;
    border-radius: 50%;
    background: var(--brand-green);
  }
  .holder-name {
    margin: 0;
    font-size: 24px;
    font-weight: 700;
    letter-spacing: 0.3px;
    color: var(--ink-dark);
    white-space: nowrap;
  }
  .divider {
    position: absolute;
    left: 0;
    right: 0;
    top: 185px;
    height: 1.5px;
    background: var(--rule);
  }
  .contact-list {
    position: absolute;
    left: 56px;
    top: 215px;
    margin: 0;
    padding: 0;
    list-style: none;
    font-size: 15px;
    color: var(--ink-muted);
  }
  .contact-item {
    display: flex;
    align-items: center;
    gap: 14px;
    height: 32px;
  }
  .contact-icon {
    width: 16px;
    height: 16px;
    fill: none;
    stroke: var(--ink-muted);
    stroke-width: 1.6;
  }
</style>
</head>
<body>
  <article class="business-card">
    <div class="leaf-motif" role="img" aria-label="Large faint leaf decoration"></div>

    <header class="card-header">
      <div class="brand-name"><span class="brand-dot"></span>Verdant Harvest Collective</div>
      <h1 class="holder-name">MATEO SALVATIERRA</h1>
    </header>
    <div class="divider"></div>

    <ul class="contact-list">
      <li class="contact-item">
        <svg class="contact-icon" viewBox="0 0 16 16" aria-hidden="true"><path d="M4 1.5h2.5l1 3.5-1.8 1.2a8 8 0 0 0 4 4l1.2-1.8 3.5 1v2.6c0 .8-.7 1.5-1.5 1.5A12 12 0 0 1 2.5 3c0-.8.7-1.5 1.5-1.5z"/></svg>
        <span>0412558390</span>
      </li>
      <li class="contact-item">
        <svg class="contact-icon" viewBox="0 0 16 16" aria-hidden="true"><rect x="1.5" y="3.5" width="13" height="9" rx="1"/><path d="M1.5 4l6.5 5 6.5-5"/></svg>
        <span>hello@verdantharvest.com</span>
      </li>
      <li class="contact-item">
        <svg class="contact-icon" viewBox="0 0 16 16" aria-hidden="true"><circle cx="8" cy="8" r="6.5"/><path d="M1.5 8h13M8 1.5c2 2 2 11 0 13M8 1.5c-2 2-2 11 0 13"/></svg>
        <span>www.verdantharvest.com</span>
      </li>
    </ul>
  </article>
</body>
</html>
```